Website for CIO outsourcing company
Velmont Systems, LLC
Website for CIO outsourcing company - Information Technology
Creative Brief
Information Technology
www.govelmontexample.com
Velmont knows that IT plays a central role to each business, and can be a determining factor in the success or failure of that business. As a committed partner we are looking for the right balance between user experience and employee satisfaction, and achieve this through care, communication and sustainable solutions. To accomplish this Velmont works closely with our clients to offer the best IT solutions to support their business processes.
Services: IT Automation: Outsourcing Project Services 360 degree Consultation & Review Need Friendlane, Linkwork and Chirpline integration. Font: Linux Libertine
Modern
Colors that work with logo
left side
www.brandeko.example.co.uk
www.plexorvanta.example.nl
www.hwtnet.example.net
Content-wise (translation to English) www.dorvenkaal-ict.example.nl/ is the site that has the kind of verbiage we are looking for.

```html
<!DOCTYPE html>
<html lang="en">
<head>
<meta charset="utf-8">
<title>Velmont Systems, LLC</title>
<link rel="stylesheet" href="https://fonts.googleapis.com/css2?family=Libertinus+Serif:wght@400;600&family=Open+Sans:wght@400;600&display=swap">
<style>
:root{
  --red:#b5121b;
  --nav:#5c6367;
  --panel:#1e2a30;
  --bg-top:#b9c5ca;
  --bg-bottom:#8e9ea5;
  --white:#ffffff;
  --ink:#3a3f42;
  --partner-ink:#3b4144;
  --copy:#d6dbdd;
  --serif:"Libertinus Serif", "Linux Libertine", Georgia, serif;
  --sans:"Open Sans", Arial, sans-serif;
}
*{box-sizing:border-box;margin:0;padding:0}
html,body{width:1200px;height:988px;overflow:hidden}
body{position:relative;font-family:var(--serif);color:var(--ink);
  background:linear-gradient(180deg,var(--bg-top) 0%,#a5b3b9 45%,var(--bg-bottom) 100%)}
.backdrop{position:absolute;left:0;top:75px;width:1200px;height:913px;
  background:linear-gradient(90deg,rgba(90,105,112,.35) 0%,rgba(160,176,182,.15) 40%,rgba(120,135,142,.35) 100%)}
.site-header{position:absolute;left:0;top:0;width:1200px;height:75px;background:var(--white)}
.brand{position:absolute;left:187px;top:14px;display:flex;align-items:center;gap:8px}
.brand-dot{width:22px;height:22px;border-radius:50%;background:var(--red)}
.brand-name{font-family:var(--serif);font-size:34px;color:var(--red);letter-spacing:1px;text-transform:uppercase}
.login{position:absolute;left:968px;top:6px;font-family:var(--sans);font-size:11px;color:var(--ink);display:flex;align-items:center;gap:6px}
.login-box{width:14px;height:12px;background:var(--ink)}
.search{position:absolute;left:803px;top:32px;width:215px;height:26px;background:#e6e8e9;
  font-family:var(--sans);font-size:11px;color:#a5a9ab;padding:5px 10px}
.search svg{position:absolute;right:8px;top:6px}
.nav{position:absolute;left:182px;top:97px;width:208px;height:305px;background:var(--nav);padding:20px 0 0 28px}
.nav li{list-style:none;font-family:var(--serif);font-size:15px;line-height:23px;color:var(--white)}
.hero{position:absolute;left:397px;top:97px;width:621px;height:305px;
  background:linear-gradient(135deg,#e8f2f8 0%,#9fc0d6 35%,#5a88aa 65%,#c9dbe6 100%)}
.tiles{position:absolute;left:182px;top:410px;width:836px;display:grid;grid-template-columns:repeat(4,1fr);gap:6px}
.tile{height:201px;background:var(--white);position:relative}
.tile-photo{height:129px;border-bottom:3px solid var(--red)}
.tile-photo.dark{background:linear-gradient(135deg,#2c3236,#5a6266)}
.tile-photo.light{background:linear-gradient(135deg,#d9dbdc,#8f9496)}
.tile-photo.warm{background:linear-gradient(135deg,#e2dcd4,#9a958f)}
.tile-photo.soft{background:linear-gradient(135deg,#ece6df,#b8aea3)}
.tile-title{font-family:var(--serif);font-size:15px;font-weight:400;line-height:18px;color:var(--red);padding:8px 12px 0;width:150px}
.tile-more{position:absolute;right:8px;bottom:8px}
.social{position:absolute;left:182px;top:632px;width:208px;height:198px;display:grid;
  grid-template-columns:101px 101px;grid-template-rows:97px 97px;gap:4px 6px}
.social-tile{background:var(--red);color:var(--white);display:flex;align-items:center;justify-content:center;
  font-family:var(--serif);font-size:15px}
.about{position:absolute;left:397px;top:632px;width:621px;height:198px;background:var(--panel);color:var(--white)}
.about-mark{position:absolute;left:50px;top:52px;width:96px;height:96px;border:2px solid var(--white);border-radius:50%;
  display:flex;align-items:center;justify-content:center;font-family:var(--serif);font-size:18px}
.about-title{position:absolute;left:192px;top:26px;font-size:20px;font-weight:400}
.about-copy{position:absolute;left:192px;top:60px;width:400px;font-size:11.5px;line-height:16px;color:var(--copy)}
.partners{position:absolute;left:182px;top:860px;width:836px;height:34px;display:flex;align-items:center;justify-content:space-between;padding:0 30px 0 36px}
.partner-badge{width:36px;height:34px;background:#2b2f31}
.partner{font-family:var(--sans);font-size:14px;color:var(--partner-ink);font-weight:600}
.footer-rule{position:absolute;left:182px;top:928px;width:836px;height:1px;background:rgba(255,255,255,.7)}
.footer{position:absolute;left:182px;top:948px;width:836px;display:flex;justify-content:space-between;
  font-family:var(--sans);font-size:10px;color:var(--white);letter-spacing:.3px}
.footer-links{display:flex;gap:26px}
</style>
</head>
<body>
<div class="backdrop" role="img" aria-label="Faded city skyline with a bridge behind the page"></div>

<header class="site-header">
  <div class="brand"><span class="brand-dot"></span><span class="brand-name">Velmont</span></div>
  <div class="login">login <span class="login-box"></span></div>
  <div class="search">Search
    <svg width="14" height="14" viewBox="0 0 14 14"><circle cx="6" cy="6" r="4.5" fill="none" stroke="#a5a9ab" stroke-width="1.5"/><line x1="9.3" y1="9.3" x2="13" y2="13" stroke="#a5a9ab" stroke-width="1.5"/></svg>
  </div>
</header>

<nav class="nav">
  <ul>
    <li>Home</li><li>Managed Services</li><li>IT Solutions</li><li>Cloud 365</li>
    <li>Web Development</li><li>Why Brandeko</li><li>News &amp; Insight</li><li>Contact Us</li><li>Remote</li>
  </ul>
</nav>

<div class="hero" role="img" aria-label="Business people in silhouette by a glass office window"></div>

<section class="tiles">
  <article class="tile"><div class="tile-photo dark" role="img" aria-label="Server room racks"></div><h3 class="tile-title">IT Automation</h3>
    <svg class="tile-more" width="14" height="14" viewBox="0 0 14 14"><circle cx="7" cy="7" r="6" fill="none" stroke="#999"/><path d="M4.5 5.5 7 8 9.5 5.5" fill="none" stroke="#999"/></svg></article>
  <article class="tile"><div class="tile-photo light" role="img" aria-label="Office team at work"></div><h3 class="tile-title">Outsourcing</h3>
    <svg class="tile-more" width="14" height="14" viewBox="0 0 14 14"><circle cx="7" cy="7" r="6" fill="none" stroke="#999"/><path d="M4.5 5.5 7 8 9.5 5.5" fill="none" stroke="#999"/></svg></article>
  <article class="tile"><div class="tile-photo warm" role="img" aria-label="Colleagues in a meeting"></div><h3 class="tile-title">Project Services</h3>
    <svg class="tile-more" width="14" height="14" viewBox="0 0 14 14"><circle cx="7" cy="7" r="6" fill="none" stroke="#999"/><path d="M4.5 5.5 7 8 9.5 5.5" fill="none" stroke="#999"/></svg></article>
  <article class="tile"><div class="tile-photo soft" role="img" aria-label="Group reviewing work at a table"></div><h3 class="tile-title">360 degree Consultation &amp; Review</h3>
    <svg class="tile-more" width="14" height="14" viewBox="0 0 14 14"><circle cx="7" cy="7" r="6" fill="none" stroke="#999"/><path d="M4.5 5.5 7 8 9.5 5.5" fill="none" stroke="#999"/></svg></article>
</section>

<section class="social">
  <div class="social-tile">Friendlane</div>
  <div class="social-tile">Linkwork</div>
  <div class="social-tile">Chirpline</div>
  <div class="social-tile" aria-label="Email">
    <svg width="40" height="28" viewBox="0 0 40 28"><rect x="1" y="1" width="38" height="26" fill="#fff"/><path d="M1 1 20 16 39 1" fill="none" stroke="#b5121b" stroke-width="3"/></svg>
  </div>
</section>

<section class="about">
  <div class="about-mark">Velmont</div>
  <h2 class="about-title">Velmont knows that IT</h2>
  <p class="about-copy">plays a central role to each business, and can be a determining factor in the success or failure of that business. As a committed partner we are looking for the right balance between user experience and employee satisfaction, and achieve this through care, communication and sustainable solutions. To accomplish this Velmont works closely with our clients to offer the best IT solutions to support their business processes.</p>
</section>

<section class="partners">
  <span class="partner-badge"></span>
  <span class="partner">Quorvane</span>
  <span class="partner">Zentrilo</span>
  <span class="partner">Maxtorvel</span>
  <span class="partner">Plurandi</span>
  <span class="partner">Ostrevik</span>
  <span class="partner">Hovralun</span>
</section>

<div class="footer-rule"></div>
<footer class="footer">
  <span>VELMONT SYSTEMS, LLC © 2013</span>
  <span class="footer-links"><span>PRIVACY POLICY</span><span>TERMS &amp; CONDITIONS</span><span>SITEMAP</span><span>CONTACT</span></span>
</footer>
</body>
</html>
```